Build a landing page to promote a service (dialler consultation and support).

We are a call centre consultation firm and we need a landing page to promote a service. The service is Morvexa dialler consultation and support.
If you do not know what Morvexa is, please do some quick "Zumbrel" research for more information.
The landing page will be promoted with a paid advertisement, so we want something that is simple, and explains exactly what service we offer.
There are two objectives for the landing page:
1) A "call to action" which directs the user to a contact page, including a form plus all of our contact details.
2) A form for them viewers to enter their details to get a "FREE" quote for their project. This form should be placed on the main page.
Notes:
The call to action will require the viewer to enter their name, email, phone number as well as a description of their request. There will also need to be a drop down menu for the type of quote. This menu should have the following options:
1) Morvexa support
2) Morvexa hosting
3) Morvexa customisation
4) Other
We need 2 pages in total:
1) Main landing page
This is the home page. It will need to clearly indicate our services and our key selling features.
Services:
* Morvexa support
* Morvexa hosting
* Morvexa customisation
Key Selling Features:
* Australian based
* PCI complaint
* 10+ years of dialler and call centre experience
* we run a sister company which is a highly reputable 40 seat call centre, so we know first hand about call centre technology.
The main landing page will have an "about us" section with a few paragraphs about how we got started.
-------------------------------------------------------------------------
2) Contact page
All of our contact details will live on this page, as well as a contact form.
Other notes:
We will be self hosting the landing page.
We already have a domain name.
The design must be clean and incorporate our logo, as well as it's colours. (Logo attached)
We want a fully function HTML landing page, not just a "PSD" design.
The page must be mobile optimised.
Anyone using Morvexa software.

```html
<!DOCTYPE html>
<html lang="en">
<head>
<meta charset="utf-8">
<title>Brightwell – Morvexa Consultation &amp; Support</title>
<link rel="stylesheet" href="https://fonts.googleapis.com/css2?family=Jost:wght@400;500;600;700&family=Montserrat:wght@600;700&display=swap">
<style>
:root{
  --teal:#1fb39a;
  --teal-dark:#16967f;
  --blue:#1a8fd1;
  --blue-deep:#0f6fb0;
  --ink:#2b2b2b;
  --text:#4a4a4a;
  --grey-bg:#f1f1f1;
  --card:#f2f2f2;
  --white:#ffffff;
  --footer-dark:#1d2630;
}
*{box-sizing:border-box;margin:0;padding:0}
html,body{width:1200px;height:2612px;overflow:hidden}
body{position:relative;background:var(--white);font-family:"Jost",sans-serif;color:var(--text)}
.abs{position:absolute}

/* header */
.site-header{position:absolute;left:0;top:0;width:1200px;height:64px;background:var(--white);z-index:5}
.contact-mini{position:absolute;top:22px;display:flex;align-items:center;gap:10px;font-size:14px;color:var(--ink)}
.brand-halo{position:absolute;left:500px;top:-30px;width:200px;height:200px;border-radius:50%;background:var(--white);z-index:6;display:flex;flex-direction:column;align-items:center;justify-content:flex-end;padding-bottom:48px}
.brand-dot{width:48px;height:48px;border-radius:50%;background:var(--blue);margin-bottom:8px}
.brand-name{font-size:26px;font-weight:500;color:var(--blue);line-height:1}
.social{position:absolute;top:19px;left:943px;display:flex;gap:6px}
.social span{width:25px;height:25px;border-radius:50%;display:block}

/* buttons */
.btn{position:absolute;display:flex;align-items:center;height:30px;border-radius:15px;background:var(--teal);color:var(--white);font-weight:600;font-size:13px;letter-spacing:.3px;padding-left:18px}
.btn .knob{position:absolute;right:-6px;top:-4px;width:38px;height:38px;border-radius:50%;background:var(--white);border:3px solid var(--blue)}
.btn .knob::after{content:"";position:absolute;left:7px;top:7px;width:18px;height:18px;border-radius:50%;background:var(--blue)}
.btn.light{background:var(--white);color:var(--blue-deep)}

/* hero */
.hero-photo{position:absolute;left:0;top:64px;width:1200px;height:600px;background:linear-gradient(100deg,#eef0f1 0%,#e3e6e8 38%,#aab4bd 62%,#56606c 82%,#2e3a4a 100%)}
.hero-title{position:absolute;left:143px;top:280px;font-family:"Montserrat",sans-serif;font-weight:700;font-size:31px;line-height:43px;color:var(--ink)}

/* about */
.section-title{font-size:30px;font-weight:500;color:var(--blue)}
.section-title .accent{color:var(--teal)}
.about-lead{position:absolute;left:143px;top:802px;width:520px;font-size:12.5px;line-height:19px;font-weight:600;color:var(--ink)}
.about-body{position:absolute;left:143px;top:853px;width:520px;font-size:12.5px;line-height:21px;color:var(--text)}

/* quote form */
.quote-card{position:absolute;left:707px;top:731px;width:351px;height:363px;background:var(--grey-bg);border-radius:6px;border:1px solid #e4e4e4}
.quote-head{height:65px;background:var(--blue);border-radius:6px 6px 0 0;color:var(--white);font-size:21px;font-weight:600;text-align:center;line-height:65px;position:relative}
.quote-head::after{content:"";position:absolute;left:50%;bottom:-12px;margin-left:-12px;border:12px solid transparent;border-bottom:0;border-top-color:var(--blue)}
.field{position:absolute;left:19px;width:314px;height:38px;background:var(--white);border:1px solid #dcdcdc;border-radius:3px;font-size:12.5px;color:var(--ink);padding-left:16px;line-height:36px}

/* services */
.services{position:absolute;left:0;top:1163px;width:1200px;height:445px;background:var(--grey-bg)}
.service{position:absolute;top:125px;width:300px;text-align:center}
.service-photo{width:154px;height:154px;border-radius:50%;margin:0 auto;border:4px solid var(--teal);padding:4px;background-clip:content-box}
.service h3{margin-top:20px;font-size:18px;font-weight:500;color:var(--blue)}
.service p{margin-top:10px;font-size:12.5px;line-height:18px;color:var(--ink)}

/* band */
.cta-band{position:absolute;left:0;top:1608px;width:1200px;height:270px;background:linear-gradient(90deg,#2a8fcf,#3a9fdc 55%,#2e93d2)}
.cta-band p{position:absolute;left:0;top:72px;width:1200px;text-align:center;font-size:21px;line-height:35px;color:var(--white)}

/* why */
.feature{position:absolute;top:2008px;width:280px;height:267px;background:var(--card);border-radius:4px;text-align:center}
.feature-icon{width:98px;height:98px;border-radius:50%;background:var(--white);margin:33px auto 0;position:relative}
.feature h3{margin-top:20px;font-size:15.5px;line-height:18px;font-weight:500;color:var(--ink)}
.feature p{margin-top:14px;font-size:12.5px;line-height:18px;color:var(--ink)}
.feature .more{position:absolute;left:123px;bottom:-17px;width:34px;height:34px;border-radius:50%;background:var(--white);box-shadow:0 1px 4px rgba(0,0,0,.12);color:var(--teal);font-size:16px;line-height:34px;font-weight:600}

/* footer */
.footer-photo{position:absolute;left:0;top:2386px;width:1200px;height:192px;background:linear-gradient(180deg,#3b4650 0%,#222c36 60%,#1a222b 100%)}
.footer-item{position:absolute;top:2482px;display:flex;align-items:center;gap:12px;color:var(--white);font-size:12.5px;line-height:16px}
.round-icon{width:34px;height:34px;border-radius:50%;background:var(--blue);display:flex;align-items:center;justify-content:center;flex-shrink:0}
.copyright{position:absolute;left:0;top:2578px;width:1200px;height:34px;background:var(--blue)}
.copyright span{position:absolute;left:143px;top:9px;font-size:11px;color:var(--white)}
.copyright .social{top:5px;left:933px}
.copyright .social span{border:1.5px solid var(--white);background:transparent;width:24px;height:24px}
</style>
</head>
<body>

<header class="site-header">
  <div class="contact-mini" style="left:143px">
    <svg width="18" height="18" viewBox="0 0 24 24" fill="none" stroke="#1a8fd1" stroke-width="2"><path d="M5 3h4l2 5-3 2a12 12 0 0 0 6 6l2-3 5 2v4a2 2 0 0 1-2 2A17 17 0 0 1 3 5a2 2 0 0 1 2-2z"/></svg>
    555-014-2290
  </div>
  <div class="contact-mini" style="left:285px;font-size:12.5px">
    <svg width="18" height="14" viewBox="0 0 24 18" fill="none" stroke="#1a8fd1" stroke-width="2"><rect x="1" y="1" width="22" height="16" rx="2"/><path d="M1 2l11 8 11-8"/></svg>
    hello@brightwelldial.com
  </div>
  <a class="btn" style="left:772px;top:16px;width:140px">Get A Quote<span class="knob"></span></a>
  <div class="social">
    <span style="background:#3b5998"></span>
    <span style="background:#55acee"></span>
    <span style="background:#0077b5"></span>
    <span style="background:#dd4b39"></span>
  </div>
</header>

<div class="brand-halo"><span class="brand-dot"></span><span class="brand-name">Brightwell</span></div>

<section>
  <div class="hero-photo" role="img" aria-label="Photo of two businessmen in an office reviewing a tablet together"></div>
  <svg class="abs" style="left:0;top:540px" width="1200" height="140" viewBox="0 0 1200 140">
    <path d="M0 40 Q600 185 1200 40 L1200 140 L0 140 Z" fill="#ffffff"/>
    <path d="M0 52 Q600 200 1200 52" fill="none" stroke="#1fb39a" stroke-width="3"/>
  </svg>
  <h1 class="hero-title">We Are A Call Center<br>Consultation &amp; Support<br>Firm For Morvexa Software</h1>
</section>

<section>
  <h2 class="section-title abs" style="left:143px;top:748px">About <span class="accent">Brightwell</span></h2>
  <p class="about-lead">Lorem ipsum dolor sit amet, consectetuer adipiscing elit, sed diam nonummy nibh smod tincidunt ut laoreet dolore magna aliquam erat volutpat.</p>
  <p class="about-body">Lorem ipsum dolor sit amet, consectetuer adipiscing elit, sed diam nonummy nibh euismod tincidunt ut laoreet dolore magna aliquam erat volutpat. Ut wisi enim ad minim veniam, quis nostrud exerci tation ullamcorper suscipit lobortis nisl ut aliquip ex ea commodo consequat. Duis autem vel eum iriure dolor in hendrerit in vulputate velit esse molestie consequat, vel illum dolore eu feugiat nulla facilisis at vero eros et accumsan et iusto odio dignissim qui blandit praesent luptatum zzril delenit augue duis dolore te feugait nulla facilisi. Lorem ipsum dolor sit amet, consectetuer adipiscing elit.</p>
  <a class="btn" style="left:143px;top:1030px;width:172px">Contact Us Today<span class="knob"></span></a>

  <form class="quote-card">
    <div class="quote-head">Request A Quote</div>
    <div class="field" style="top:97px">Name</div>
    <div class="field" style="top:144px">Email</div>
    <div class="field" style="top:191px">Phone</div>
    <div class="field" style="top:240px">Quote for
      <svg class="abs" style="right:14px;top:15px" width="9" height="6" viewBox="0 0 9 6"><path d="M1 1l3.5 3.5L8 1" fill="none" stroke="#555" stroke-width="1.3"/></svg>
    </div>
    <a class="btn" style="left:101px;top:299px;width:140px">Submit Now<span class="knob"></span></a>
  </form>
</section>

<section class="services">
  <h2 class="section-title abs" style="left:0;top:60px;width:1200px;text-align:center;color:var(--teal)"><span style="color:var(--blue)">Our</span> Services</h2>
  <div class="service" style="left:134px">
    <div class="service-photo" role="img" aria-label="Photo of call centre agents wearing headsets" style="background-color:#b88a6e;background-image:linear-gradient(135deg,#e8d6c8,#9c6c52)"></div>
    <h3>Morvexa Support</h3>
    <p>Lorem ipsum dolor sit amet, consectetuer<br>adipiscing elit, sed diam nonummy nibh smod<br>tincidunt ut laoreet dolore magna aliquam.</p>
  </div>
  <div class="service" style="left:451px">
    <div class="service-photo" role="img" aria-label="Illustration of servers with a laptop and monitor" style="background-image:linear-gradient(135deg,#5fb4e8,#1f5f9e)"></div>
    <h3>Morvexa Hosting</h3>
    <p>Lorem ipsum dolor sit amet, consectetuer<br>adipiscing elit, sed diam nonummy nibh smod<br>tincidunt ut laoreet dolore magna aliquam.</p>
  </div>
  <div class="service" style="left:768px">
    <div class="service-photo" role="img" aria-label="Photo of hands typing on a keyboard" style="background-image:linear-gradient(135deg,#f2f4f6,#9aa7b2)"></div>
    <h3>Morvexa Customization</h3>
    <p>Lorem ipsum dolor sit amet, consectetuer<br>adipiscing elit, sed diam nonummy nibh smod<br>tincidunt ut laoreet dolore magna aliquam.</p>
  </div>
</section>

<section class="cta-band" role="img" aria-label="Blue-tinted photo of a call centre office with monitors">
  <p>Lorem ipsum dolor sit amet, consectetuer adipiscing elit, sed diam nonummy<br>nibh smod tincidunt ut laoreet dolore magna aliquam erat volutpat.</p>
  <a class="btn light" style="left:511px;top:157px;width:172px">Contact Us Today<span class="knob"></span></a>
</section>

<section>
  <h2 class="section-title abs" style="left:0;top:1938px;width:1200px;text-align:center;color:var(--teal)">Why Choose Us</h2>
  <div class="feature" style="left:143px">
    <div class="feature-icon"><svg class="abs" style="left:27px;top:30px" width="44" height="38" viewBox="0 0 44 38"><rect x="2" y="2" width="40" height="34" rx="8" fill="none" stroke="#1fb39a" stroke-width="2"/></svg></div>
    <h3>Australian Based</h3>
    <p>Lorem ipsum dolor sit amet, consectetuer<br>adipiscing elit, sed diam nonummy.</p>
    <div class="more">»</div>
  </div>
  <div class="feature" style="left:460px">
    <div class="feature-icon"><svg class="abs" style="left:27px;top:24px" width="44" height="50" viewBox="0 0 44 50"><path d="M22 2l18 7v16c0 12-8 19-18 23C12 44 4 37 4 25V9z" fill="none" stroke="#1fb39a" stroke-width="2"/></svg></div>
    <h3>10+ Years of Dialler &amp;<br>Call Centre Experience</h3>
    <p>Lorem ipsum dolor sit amet, consectetuer<br>adipiscing elit, sed diam nonummy.</p>
    <div class="more">»</div>
  </div>
  <div class="feature" style="left:779px">
    <div class="feature-icon"><svg class="abs" style="left:25px;top:30px" width="48" height="38" viewBox="0 0 48 38"><rect x="2" y="2" width="40" height="28" rx="3" fill="none" stroke="#1fb39a" stroke-width="2"/><line x1="2" y1="11" x2="42" y2="11" stroke="#1fb39a" stroke-width="2"/><rect x="30" y="22" width="14" height="12" rx="2" fill="#ffffff" stroke="#1fb39a" stroke-width="2"/></svg></div>
    <h3>PCI Compliant</h3>
    <p>Lorem ipsum dolor sit amet, consectetuer<br>adipiscing elit, sed diam nonummy.</p>
    <div class="more">»</div>
  </div>
</section>

<footer>
  <div class="footer-photo" role="img" aria-label="Photo of a city skyline and river at dusk"></div>
  <svg class="abs" style="left:0;top:2380px" width="1200" height="90" viewBox="0 0 1200 90">
    <path d="M0 0 H1200 V84 Q600 -8 0 84 Z" fill="#ffffff"/>
    <path d="M0 80 Q600 -14 1200 80" fill="none" stroke="#1fb39a" stroke-width="3"/>
  </svg>
  <div class="abs" style="left:562px;top:2350px;width:76px;height:76px;border-radius:50%;background:var(--white);border:4px solid var(--teal)"></div>
  <div class="abs" style="left:581px;top:2369px;width:38px;height:38px;border-radius:50%;background:var(--blue)"></div>

  <div class="footer-item" style="left:312px">
    <span class="round-icon"><svg width="12" height="16" viewBox="0 0 12 16"><path d="M6 1a5 5 0 0 1 5 5c0 4-5 9-5 9S1 10 1 6a5 5 0 0 1 5-5z" fill="#fff"/><circle cx="6" cy="6" r="2" fill="#1a8fd1"/></svg></span>
    <span>14/30 Harbour Vale Road<br>Kelmont, QLD 4511</span>
  </div>
  <div class="footer-item" style="left:544px">
    <span class="round-icon"><svg width="15" height="15" viewBox="0 0 24 24" fill="#fff"><path d="M5 3h4l2 5-3 2a12 12 0 0 0 6 6l2-3 5 2v4a2 2 0 0 1-2 2A17 17 0 0 1 3 5a2 2 0 0 1 2-2z"/></svg></span>
    <span>Phone<br>555-014-2290</span>
  </div>
  <div class="footer-item" style="left:728px">
    <span class="round-icon"><svg width="16" height="12" viewBox="0 0 24 18"><rect x="1" y="1" width="22" height="16" rx="2" fill="#fff"/><path d="M1 2l11 8 11-8" fill="none" stroke="#1a8fd1" stroke-width="2"/></svg></span>
    <span>Email<br>hello@brightwelldial.com</span>
  </div>

  <div class="copyright">
    <span>Copyright © 2018 Brightwell. All Rights Reserved</span>
    <div class="social"><span></span><span></span><span></span><span></span></div>
  </div>
</footer>

</body>
</html>
```